The Corvane Agency

We are a pr, social media and strategy agency specializing in the pet industry. We would like a new dynamic design of our existing website. We think it is currently outdated and looks too corporate. We would like it to look more consumer oriented as we primarily market pet products. We would like warm imagery involving pets and while pets are fun, this is still a business website and needs to maintain a professional look. We are hired by business owners and executives.
I would like some of our work featured on the home page.
Our primary service tabs are:
Public Relations
Social Media
Product Consulting
Most of the content will remain the same but we are open to suggestions!
Our current website can be found at www.lorvishdogpr.com.
We are open to other colors than in our logo and on our current page.
This is a design only project and will not require programming. The selected designer will need to provide at least one interior page in addition to the home page.

Industry/Entity Type

Pet

Requirements
Should not have
• Cartoon type figures. Pet puns.

```html
<!DOCTYPE html>
<html lang="en">
<head>
<meta charset="utf-8">
<title>The Corvane Agency</title>
<link href="https://fonts.googleapis.com/css2?family=Oswald:wght@500;700&family=Ubuntu:wght@400;500&display=swap" rel="stylesheet">
<style>
:root{
  --red:#d9000d;
  --red-dark:#b30009;
  --ink:#222;
  --text:#444;
  --grey-band:#ebebeb;
  --line:#d6d6d6;
  --footer:#3a3a3a;
  --footer-base:#2a2a2a;
  --ribbon-grey:#6b6b6b;
}
*{box-sizing:border-box;margin:0;padding:0}
html,body{width:811px;height:1200px;overflow:hidden;background:#fff}
body{position:relative;font-family:'Ubuntu',sans-serif;color:var(--text)}
.abs{position:absolute}
a{color:inherit;text-decoration:none}

/* header */
.brand{left:100px;top:22px;font-size:30px;font-weight:500;color:var(--red);letter-spacing:-.5px;display:flex;align-items:center;gap:7px}
.brand-dot{width:9px;height:9px;border-radius:50%;background:var(--red)}
.social-top{left:620px;top:13px;display:flex;gap:6px}
.social-top span{width:20px;height:20px;border-radius:3px;background:#fff;border:1px solid #ddd;box-shadow:0 1px 2px rgba(0,0,0,.2);display:flex;align-items:center;justify-content:center}
.social-top span i{width:9px;height:9px;background:var(--red);border-radius:2px;display:block}
.phone-top{left:581px;top:42px;display:flex;align-items:center;gap:8px;font-size:15px;font-weight:500;color:var(--ink)}
.phone-top .ring{width:24px;height:24px;border-radius:50%;background:var(--red);display:flex;align-items:center;justify-content:center}

/* nav */
.nav{left:0;top:77px;width:811px;height:29px;background:linear-gradient(#e3000f,#c0000a);display:flex;padding-left:95px}
.nav a{color:#fff;font-size:11px;font-weight:500;line-height:29px;padding:0 11px;border-right:1px solid rgba(255,255,255,.35)}
.nav a:last-child{border-right:0}
.nav a.current{background:#555;padding:0 10px}

/* hero */
.hero-photo{left:240px;top:106px;width:571px;height:298px;background:linear-gradient(90deg,#fafafa 0%,#e9d8c4 25%,#c99a6c 45%,#f2efe9 62%,#f0dcc8 80%,#e7e2dc 100%)}
.hero-rule{left:0;top:403px;width:811px;height:2px;background:#d9d9d9}
.ribbon{left:0;height:35px;width:240px;clip-path:polygon(0 0,100% 0,82% 100%,0 100%);font-family:'Oswald',sans-serif;font-weight:700;font-size:27px;color:#fff;line-height:35px;padding-left:94px;text-shadow:0 1px 2px rgba(0,0,0,.35)}
.ribbon.grey{background:linear-gradient(90deg,#5d5d5d,#a3a3a3)}
.ribbon.red{background:linear-gradient(90deg,#e01f2a,#f07a7e)}
.dots{left:95px;top:381px;display:flex;gap:4px}
.dots i{width:9px;height:9px;background:#666;display:block}
.dots i.on{background:var(--red)}

/* welcome */
.sec-title{font-size:18px;font-weight:500;color:var(--ink)}
.sec-title em{font-style:normal;color:var(--red)}
.welcome-title{left:95px;top:421px}
.welcome-rule{left:95px;top:448px;width:399px;height:1px;background:var(--line)}
.portrait{left:95px;top:459px;width:106px;height:97px;border:1px solid #ccc;padding:3px;background:#fff}
.portrait div{width:100%;height:100%;background:linear-gradient(#f4f4f4,#d9c4b2 60%,#2f3a4a)}
.welcome-copy{left:211px;top:457px;width:285px;font-size:8.6px;line-height:12.4px}
.welcome-copy p{margin-bottom:3px}
.btn-red{left:96px;top:570px;width:76px;height:21px;background:var(--red);border-radius:3px;color:#fff;font-size:11px;font-weight:500;text-align:center;line-height:21px;box-shadow:0 0 0 1px #fff inset}
.vdivider{left:510px;top:430px;height:162px;border-left:1px dotted #aaa}
.video-title{left:526px;top:421px}
.video-rule{left:526px;top:448px;width:190px;height:1px;background:var(--line)}
.video{left:526px;top:456px;width:190px;height:126px;background:linear-gradient(120deg,#6d8a3a,#e6c9a8 40%,#c7852f 75%,#7a4a18)}
.video .play{position:absolute;left:80px;top:42px;width:30px;height:30px;border-radius:50%;background:rgba(40,40,40,.6)}
.video .bar{position:absolute;left:0;bottom:0;width:100%;height:15px;background:#222}
.video .track{position:absolute;left:35px;top:6px;width:148px;height:3px;background:#777}
.video .track i{display:block;width:10px;height:3px;background:var(--red)}

/* services */
.services{left:0;top:612px;width:811px;height:168px;background:var(--grey-band)}
.svc{position:absolute;top:16px;width:200px;text-align:center}
.svc .icon{width:72px;height:72px;border-radius:50%;background:#3a3a3a;margin:0 auto;display:flex;align-items:center;justify-content:center}
.svc h3{font-family:'Oswald',sans-serif;font-weight:500;font-size:12px;color:var(--ink);margin-top:14px;letter-spacing:.1px}
.svc p{font-size:8.5px;line-height:13px;margin-top:3px}
.svc a{font-size:8.5px;font-weight:500;color:var(--red);display:block;margin-top:3px}
.svc-rule{top:630px;width:1px;height:135px;background:linear-gradient(transparent,#ccc,transparent)}

/* boxes */
.box{top:806px;width:196px;height:176px;background:#fff;border:1px solid #ddd;box-shadow:0 6px 6px -4px rgba(0,0,0,.25)}
.box-head{height:25px;background:linear-gradient(#e3000f,#c2000a);color:#fff;font-size:14px;font-weight:500;line-height:25px;padding-left:9px;display:flex;align-items:center;gap:7px}
.corner{position:absolute;right:0;bottom:0;width:30px;height:30px;background:var(--red);clip-path:polygon(100% 0,100% 100%,0 100%)}
.corner b{position:absolute;right:4px;bottom:0;color:#fff;font-size:14px;font-weight:500}
.blog-item{margin:0 10px;padding:6px 0 5px;border-bottom:1px dotted #ccc;font-size:8px;line-height:11px}
.blog-item:last-of-type{border-bottom:0}
.blog-item strong{display:block;font-weight:500;color:var(--ink)}
.blog-item a{color:var(--red);font-weight:500}
.quote{position:absolute;left:10px;top:32px;width:174px;height:96px;border:1px solid #ccc;border-radius:4px;padding:6px 9px;font-size:8px;line-height:11.6px}
.avatar{position:absolute;left:22px;top:104px;width:62px;height:62px;border-radius:50%;border:1px solid #ccc;background:#fff;padding:3px}
.avatar div{width:100%;height:100%;border-radius:50%;background:linear-gradient(#eee,#d2b9a2 55%,#2b3442)}
.quote-name{position:absolute;left:96px;top:133px;font-size:8.5px;font-weight:500;color:var(--ink)}
.field{position:absolute;left:12px;width:170px;height:22px;border:1px solid #ccc;border-radius:3px;font-size:8px;color:#666;padding:5px 0 0 22px;box-shadow:inset 0 1px 2px rgba(0,0,0,.08)}
.field svg{position:absolute;left:7px;top:6px}
.submit{position:absolute;left:12px;top:147px;width:54px;height:18px;background:linear-gradient(#666,#3a3a3a);border-radius:3px;color:#fff;font-size:9.5px;font-weight:500;text-align:center;line-height:18px}

/* footer */
.footer{left:0;top:1016px;width:811px;height:162px;background:var(--footer);color:#eee}
.footer-base{left:0;top:1178px;width:811px;height:22px;background:var(--footer-base);color:#eee;font-size:8.5px;text-align:center;line-height:22px}
.fcol{position:absolute;top:19px}
.fcol h4{font-size:13px;font-weight:500;color:#fff;padding-bottom:4px;border-bottom:1px dotted #666;margin-bottom:7px}
.links{display:grid;grid-template-columns:103px 60px;row-gap:6.4px;font-size:8px}
.contact{font-size:8px;line-height:11px}
.contact strong{font-weight:500;font-size:9px;color:#fff}
.contact .row{display:flex;align-items:center;gap:6px;margin-top:10px}
.map{width:158px;height:88px;background:linear-gradient(135deg,#e8c88e,#d9b477 50%,#e6cb98);border:1px solid #ccc}
.follow .row{display:flex;align-items:center;gap:10px;font-size:7.8px;margin-bottom:9px}
.follow .row i{width:11px;height:11px;background:#fff;border-radius:2px;display:block}
</style>
</head>
<body>

<header>
  <div class="abs brand"><span class="brand-dot"></span>The Corvane Agency</div>
  <div class="abs social-top"><span><i></i></span><span><i></i></span><span><i></i></span><span><i></i></span></div>
  <div class="abs phone-top">
    <span class="ring"><svg width="12" height="12" viewBox="0 0 24 24"><path fill="#fff" d="M6.6 10.8a15 15 0 0 0 6.6 6.6l2.2-2.2c.3-.3.7-.4 1-.2 1.1.4 2.3.6 3.6.6.6 0 1 .4 1 1V20c0 .6-.4 1-1 1A17 17 0 0 1 3 4c0-.6.4-1 1-1h3.5c.6 0 1 .4 1 1 0 1.3.2 2.5.6 3.6.1.3 0 .7-.2 1z"/></svg></span>
    (555) 214-7730
  </div>
  <nav class="abs nav">
    <a class="current" href="#">Home</a><a href="#">PR</a><a href="#">Social Media</a><a href="#">Pet Experts</a><a href="#">Business Development</a><a href="#">Case Studies</a><a href="#">Our Team</a><a href="#">Contact Us</a>
  </nav>
</header>

<section class="hero">
  <div class="abs hero-photo" role="img" aria-label="Smiling women hugging a large mastiff dog and a small terrier"></div>
  <div class="abs ribbon grey" style="top:178px">Redefining</div>
  <div class="abs ribbon red" style="top:224px">Pet</div>
  <div class="abs ribbon grey" style="top:270px">Products</div>
  <div class="abs dots"><i class="on"></i><i></i><i></i></div>
  <div class="abs hero-rule"></div>
</section>

<section class="welcome">
  <h2 class="abs sec-title welcome-title">Welcome To <em>The Corvane Agency</em></h2>
  <div class="abs welcome-rule"></div>
  <div class="abs portrait"><div role="img" aria-label="Portrait photo of the agency founder"></div></div>
  <div class="abs welcome-copy">
    <p>Lorem ipsum dolor sit amet, consectetur adipiscing elit. Curabitur lobortis, tellus in aliquam cursus, ante lorem tristique elit, at aliquet nunc ante et orci.Pellentesque sed sodales elit.</p>
    <p>nteger quis nunc eget mauris pharetra commodo vitae in risus. Quisque sollicitudin tortor ac massa porta, eu euismod</p>
    <p>Lorem ipsum dolor sit amet, consectetur adipiscing elit. Curabitur lobortis, tellus in aliquam cursus, ante lorem tristique elit, at aliquet nunc ante et orci.Pellentesque sed sodales elit.</p>
  </div>
  <a class="abs btn-red" href="#">READ MORE</a>
  <div class="abs vdivider"></div>
  <h2 class="abs sec-title video-title">Our <em>Video</em></h2>
  <div class="abs video-rule"></div>
  <div class="abs video" role="img" aria-label="Video still of a woman cuddling a golden retriever">
    <div class="play"><svg width="30" height="30"><path d="M12 9l9 6-9 6z" fill="#fff"/></svg></div>
    <div class="bar">
      <svg width="30" height="15" style="position:absolute;left:4px;top:0"><path d="M2 4l5 3.5-5 3.5z" fill="#fff"/><rect x="14" y="4" width="2" height="7" fill="#fff"/><rect x="18" y="4" width="2" height="7" fill="#fff"/></svg>
      <div class="track"><i></i></div>
    </div>
  </div>
</section>

<section class="abs services">
  <div class="svc" style="left:96px">
    <div class="icon"><svg width="40" height="26" viewBox="0 0 40 26" fill="#fff"><circle cx="10" cy="6" r="4"/><circle cx="20" cy="5" r="4.5"/><circle cx="30" cy="6" r="4"/><path d="M2 24c0-6 4-10 8-10s8 4 8 10zM11 25c0-7 4-11 9-11s9 4 9 11zM22 24c0-6 4-10 8-10s8 4 8 10z"/></svg></div>
    <h3>PUBLIC RELATIONS</h3>
    <p>Dorem nonummy nibh euismodol laoreet<br>dolore volutpat.</p>
    <a href="#">Read More »</a>
  </div>
  <div class="svc" style="left:302px">
    <div class="icon"><svg width="40" height="40" viewBox="0 0 40 40"><circle cx="20" cy="20" r="12" fill="none" stroke="#fff" stroke-width="3"/><g fill="#fff"><circle cx="20" cy="7" r="5"/><circle cx="20" cy="33" r="5"/><circle cx="7" cy="20" r="5"/><circle cx="33" cy="20" r="5"/></g></svg></div>
    <h3>SOCIAL MEDIA</h3>
    <p>Dorem nonummy nibh euismodol laoreet<br>dolore volutpat.</p>
    <a href="#">Read More »</a>
  </div>
  <div class="svc" style="left:514px">
    <div class="icon"><svg width="36" height="40" viewBox="0 0 36 40"><rect x="4" y="5" width="22" height="30" rx="2" fill="none" stroke="#fff" stroke-width="3"/><rect x="10" y="2" width="10" height="6" rx="1" fill="#fff"/><path d="M9 14h4M9 20h4M9 26h4" stroke="#fff" stroke-width="2.5"/><circle cx="26" cy="28" r="8" fill="#fff"/><path d="M22 28l3 3 5-6" stroke="#3a3a3a" stroke-width="2.5" fill="none"/></svg></div>
    <h3>PRODUCT CONSULTING</h3>
    <p>Dorem nonummy nibh euismodol laoreet<br>dolore volutpat.</p>
    <a href="#">Read More »</a>
  </div>
</section>
<div class="abs svc-rule" style="left:299px"></div>
<div class="abs svc-rule" style="left:510px"></div>

<section>
  <div class="abs box" style="left:95px">
    <div class="box-head"><svg width="14" height="14" viewBox="0 0 14 14" fill="none" stroke="#fff" stroke-width="2"><circle cx="3" cy="11" r="1.5" fill="#fff" stroke="none"/><path d="M2 6a6 6 0 0 1 6 6M2 2a10 10 0 0 1 10 10"/></svg>Latest Blog</div>
    <div class="blog-item"><strong>Lorem ipsum dolor sit amet</strong>Lorem ipsum dolor sit amet, consect etuer adipiscing elit, volutpat. <a href="#">Click For More</a></div>
    <div class="blog-item"><strong>Lorem ipsum dolor sit amet</strong>Lorem ipsum dolor sit amet, consect etuer adipiscing elit, volutpat. <a href="#">Click For More</a></div>
    <div class="blog-item"><strong>Lorem ipsum dolor sit amet</strong>Lorem ipsum dolor sit amet, consect adipiscing elit, volutpat. <a href="#">Click For More</a></div>
    <div class="corner"><b>+</b></div>
  </div>

  <div class="abs box" style="left:307px">
    <div class="box-head"><svg width="16" height="14" viewBox="0 0 16 14" fill="#fff"><rect x="0" y="0" width="11" height="8" rx="2"/><path d="M2 8v4l3-4z"/><rect x="6" y="5" width="10" height="7" rx="2" fill="#fff" stroke="#d0000b"/></svg>Client Testimonials</div>
    <div class="quote">“ Lorem ipsum dolor sit a constetur ut adipiscing elit, sed diam nonu nibh amet euismod tincidunt utvop laoreet dolore magna a wisi enim tincidunt utvo laoreet sed diam nonu nibh amet ”</div>
    <div class="avatar"><div role="img" aria-label="Client portrait"></div></div>
    <div class="quote-name">Mr. Lorem ipsum</div>
    <div class="corner"><b>+</b></div>
  </div>

  <div class="abs box" style="left:520px">
    <div class="box-head"><svg width="14" height="14" viewBox="0 0 14 14" fill="none" stroke="#fff" stroke-width="2"><path d="M8 2H2v10h10V7"/><path d="M6 9l1-3 5-5 2 2-5 5z" fill="#fff"/></svg>Quick Contact</div>
    <div class="field" style="top:34px"><svg width="9" height="9" viewBox="0 0 9 9" fill="#777"><circle cx="4.5" cy="2.5" r="2.2"/><path d="M0 9c0-3 2-4.5 4.5-4.5S9 6 9 9z"/></svg>Name</div>
    <div class="field" style="top:63px"><svg width="10" height="8" viewBox="0 0 10 8"><rect width="10" height="8" fill="#777"/><path d="M0 0l5 4 5-4" stroke="#fff" fill="none"/></svg>Email</div>
    <div class="field" style="top:92px;height:46px"><svg width="9" height="9" viewBox="0 0 9 9" fill="none" stroke="#777" stroke-width="1.3"><path d="M5 1H1v7h7V4"/><path d="M4 6l4-5"/></svg>Message</div>
    <div class="submit">SUBMIT</div>
  </div>
</section>

<footer>
  <div class="abs footer">
    <div class="fcol" style="left:96px;width:150px">
      <h4>Quick Links</h4>
      <div class="links">
        <a href="#">Home</a><a href="#">Our Team</a>
        <a href="#">PR</a><a href="#">Contact Us</a>
        <a href="#">Social Media</a><a href="#">Careers</a>
        <a href="#">Pet Experts</a><a href="#">Love List</a>
        <a href="#">Business Development</a><a href="#">Blog</a>
        <a href="#">Case Studies</a><a href="#">Site Map</a>
      </div>
    </div>
    <div class="fcol contact" style="left:278px;width:144px">
      <h4>Contact Detail</h4>
      <strong>The Corvane Agency</strong><br>418 Alder Crest Rd. Halden,<br>NV 89000
      <div class="row"><svg width="9" height="9" viewBox="0 0 24 24"><path fill="#fff" d="M6.6 10.8a15 15 0 0 0 6.6 6.6l2.2-2.2c.3-.3.7-.4 1-.2 1.1.4 2.3.6 3.6.6.6 0 1 .4 1 1V20c0 .6-.4 1-1 1A17 17 0 0 1 3 4c0-.6.4-1 1-1h3.5c.6 0 1 .4 1 1 0 1.3.2 2.5.6 3.6.1.3 0 .7-.2 1z"/></svg>(555) 214-7730</div>
      <div class="row"><svg width="10" height="9" viewBox="0 0 10 9" fill="#fff"><rect x="2" y="0" width="6" height="3"/><rect x="0" y="3" width="10" height="4" rx="1"/><rect x="2" y="6" width="6" height="3"/></svg>800-555-0192</div>
      <div class="row"><svg width="10" height="7" viewBox="0 0 10 7"><rect width="10" height="7" fill="#fff"/><path d="M0 0l5 4 5-4" stroke="#3a3a3a" fill="none"/></svg>info@thecorvaneagency.com</div>
    </div>
    <div class="fcol" style="left:452px;width:158px">
      <h4>View Location</h4>
      <div class="map" role="img" aria-label="Street map showing the office location"></div>
      <div style="font-size:8.5px;font-weight:500;margin-top:6px">View »</div>
    </div>
    <div class="fcol follow" style="left:642px;width:75px">
      <h4>Follow Us</h4>
      <div class="row"><i></i>Friendsly</div>
      <div class="row"><i></i>Chirper</div>
      <div class="row"><i></i>Circlet</div>
      <div class="row"><svg width="11" height="11" viewBox="0 0 14 14" fill="none" stroke="#fff" stroke-width="2"><circle cx="3" cy="11" r="1.5" fill="#fff" stroke="none"/><path d="M2 6a6 6 0 0 1 6 6M2 2a10 10 0 0 1 10 10"/></svg>RSS Feed</div>
    </div>
  </div>
  <div class="abs footer-base">© Copyright 2014, &nbsp;The Corvane Agency &nbsp;| All Rights Reserved</div>
</footer>

</body>
</html>
```